Refresh of The Marston Collective business card

Update business card design using existing primary logo. Names, numbers, etc. are too hard to read on current design.

Target Market(s)

We are a CPA firm.

Industry/Entity Type

Accountant

Contact Information for Business Card

update current card

Colors
0355a3
3176b5
85acd3
0792cd

Requirements
Must have
• Easier to read phone numbers and names
• Use existing logo
Nice to have
• We love our color scheme and current TMC logo. But the names and phone numbers are too small and card just look old and stale.

```html
<!DOCTYPE html>
<html lang="en">
<head>
<meta charset="utf-8">
<title>The Marston Collective – Business Card</title>
<link href="https://fonts.googleapis.com/css2?family=Cinzel:wght@600&family=Didact+Gothic&display=swap" rel="stylesheet">
<style>
  :root {
    --navy: #0a2a6b;
    --brand: #0355a3;
    --brand-mid: #3176b5;
    --brand-light: #85acd3;
    --accent: #0792cd;
    --paper: #ffffff;
    --grey: #5c5c5f;
    --backdrop: #3b3b3d;
  }
  * { margin: 0; padding: 0; box-sizing: border-box; }
  html, body { width: 1200px; height: 900px; overflow: hidden; }
  body { background: var(--backdrop); position: relative; font-family: "Didact Gothic", sans-serif; }

  .card { position: absolute; border-radius: 3px; box-shadow: 0 12px 30px rgba(0,0,0,.45); overflow: hidden; }

  /* Back of card */
  .card-back {
    left: 470px; top: 70px; width: 620px; height: 354px;
    background: radial-gradient(ellipse at 45% 35%, var(--brand-mid) 0%, var(--brand) 45%, #02306a 100%);
    color: var(--paper);
  }
  .card-back .lockup { position: absolute; left: 110px; top: 110px; display: flex; align-items: center; gap: 22px; }
  .card-back .lockup-mark { width: 86px; height: 86px; border-radius: 50%; background: var(--paper); flex: none; }
  .card-back .lockup-name { font-family: "Cinzel", serif; font-weight: 600; font-size: 30px; line-height: 1.15; color: var(--paper); }
  .card-back .web { position: absolute; left: 0; right: 0; top: 262px; text-align: center; font-size: 20px; letter-spacing: .5px; }

  /* Front of card */
  .card-front { left: 110px; top: 430px; width: 680px; height: 388px; background: var(--paper); }
  .card-front .lockup { position: absolute; left: 34px; top: 30px; display: flex; align-items: center; gap: 18px; }
  .card-front .lockup-mark { width: 82px; height: 82px; border-radius: 50%; background: var(--brand); flex: none; }
  .card-front .lockup-name { font-family: "Cinzel", serif; font-weight: 600; font-size: 28px; line-height: 1.15; color: var(--navy); }
  .card-front .rule { position: absolute; left: 34px; right: 34px; top: 142px; height: 2px; background: var(--navy); }

  .contacts { position: absolute; left: 34px; top: 166px; list-style: none; }
  .contacts li { display: flex; align-items: center; gap: 10px; font-size: 19px; color: #111; line-height: 27px; }
  .contacts svg { width: 17px; height: 17px; flex: none; }

  .person { position: absolute; right: 34px; top: 160px; font-family: "Cinzel", serif; font-weight: 600; font-size: 30px; color: var(--navy); }
  .address { position: absolute; right: 34px; top: 228px; text-align: right; font-size: 19px; line-height: 26px; color: #111; }

  .footer-band { position: absolute; left: 0; bottom: 0; width: 680px; height: 58px; }
  .footer-web { position: absolute; right: 34px; bottom: 12px; color: var(--paper); font-size: 21px; letter-spacing: .5px; }
</style>
</head>
<body>

  <section class="card card-back" aria-label="Card back">
    <div class="lockup">
      <span class="lockup-mark"></span>
      <span class="lockup-name">The Marston<br>Collective</span>
    </div>
    <p class="web">www.marstoncollective.com</p>
  </section>

  <section class="card card-front" aria-label="Card front">
    <div class="lockup">
      <span class="lockup-mark"></span>
      <span class="lockup-name">The Marston<br>Collective</span>
    </div>
    <div class="rule"></div>

    <ul class="contacts">
      <li>
        <svg viewBox="0 0 20 20"><circle cx="10" cy="10" r="10" fill="var(--navy)"/><path d="M6.5 5.5l2 0 1 2.5-1.3 1a6 6 0 0 0 2.8 2.8l1-1.3 2.5 1v2a1 1 0 0 1-1 1A8.5 8.5 0 0 1 5.5 6.5a1 1 0 0 1 1-1z" fill="#fff"/></svg>
        555.318.2046
      </li>
      <li>
        <svg viewBox="0 0 20 20"><circle cx="10" cy="10" r="10" fill="var(--navy)"/><rect x="7" y="4.5" width="6" height="11" rx="1" fill="#fff"/><rect x="8" y="6" width="4" height="6.5" fill="var(--navy)"/></svg>
        555.318.2047
      </li>
      <li>
        <svg viewBox="0 0 20 20"><circle cx="10" cy="10" r="10" fill="var(--navy)"/><rect x="5" y="8" width="10" height="6" rx="1" fill="#fff"/><rect x="7" y="5" width="6" height="3.5" fill="#fff"/></svg>
        555.318.2048
      </li>
      <li>
        <svg viewBox="0 0 20 20"><circle cx="10" cy="10" r="10" fill="var(--navy)"/><rect x="5" y="6.5" width="10" height="7" fill="#fff"/><path d="M5 6.5l5 4 5-4" fill="none" stroke="var(--navy)" stroke-width="1.2"/></svg>
        dan@marstoncollective.com
      </li>
    </ul>

    <p class="person">Daniel R. Ashford, CPA</p>
    <p class="address">318 W. Harlow Ave. Suite 110<br>Lakeview, Florida 32799</p>

    <svg class="footer-band" viewBox="0 0 680 58" preserveAspectRatio="none" aria-hidden="true">
      <defs>
        <linearGradient id="bandBlue" x1="0" x2="1" y1="0" y2="0">
          <stop offset="0" stop-color="var(--brand-mid)"/>
          <stop offset="1" stop-color="var(--brand)"/>
        </linearGradient>
      </defs>
      <rect x="0" y="22" width="330" height="36" fill="var(--grey)"/>
      <path d="M300 58 C320 20 340 8 380 8 L680 8 L680 58 Z" fill="var(--paper)"/>
      <path d="M312 58 C332 26 350 14 390 14 L680 14 L680 58 Z" fill="url(#bandBlue)"/>
    </svg>
    <p class="footer-web">www.marstoncollective.com</p>
  </section>

</body>
</html>
```